Tesmaro Realty Business Cards

Design business card

Target Market(s)

High-End Buyer of Real Estate over $1 million dollars

Industry/Entity Type

Realtor

Contact Information for Business Card

Lina Tesmaro R(S) LIC.# 41927
Cell 808 555-0163
Email Lina@Tesmaro.net
Website PeakHomeFinds.com

Also Need Cards for:

Glen Tesmaro R(B) LIC# 60418
C 808 555-0192
E Glen@Tesmaro.net
W PeakHomeFinds.com

Colors

Designer to choose colors to be used in the design.

Requirements
Must have
• Address on back:
• 57 Oleander Ct. , Wailea HI 96721
• Logo on back
Nice to have
• I would like the phone numbers and email address to be big so people can read it easily
Should not have
• Very small print Except For: address (57 Oleander Ct. Wailea HI 96721)

```html
<!DOCTYPE html>
<html lang="en">
<head>
<meta charset="utf-8">
<title>Tesmaro Realty Business Cards</title>
<link rel="stylesheet" href="https://fonts.googleapis.com/css2?family=Roboto:wght@400&family=Work+Sans:wght@400;600&display=swap">
<style>
  :root {
    --stage: #121212;
    --card: #1f1f1f;
    --card-edge: #262626;
    --ink: #ffffff;
    --ink-soft: #e6e6e6;
    --photo-a: #c9a08a;
    --photo-b: #2a2a2a;
  }
  * { margin: 0; padding: 0; box-sizing: border-box; }
  html, body { width: 1200px; height: 900px; overflow: hidden; background: var(--stage); }
  .stage {
    width: 1200px; height: 900px;
    display: flex; flex-direction: column; align-items: center; justify-content: center; gap: 40px;
    font-family: "Work Sans", sans-serif; color: var(--ink);
  }
  .card {
    position: relative; width: 680px; height: 389px;
    background: linear-gradient(135deg, var(--card) 0%, var(--card-edge) 100%);
    box-shadow: 0 12px 30px rgba(0,0,0,.6);
  }
  /* back side */
  .card--back .brand {
    position: absolute; left: 50%; top: 90px; transform: translateX(-50%);
    display: flex; flex-direction: column; align-items: center; gap: 14px;
  }
  .brand__square { width: 18px; height: 18px; background: var(--ink); }
  .brand__name {
    font-weight: 600; font-size: 34px; letter-spacing: 6px; text-align: center; line-height: 1.25;
    text-transform: uppercase;
  }
  .card--back .address {
    position: absolute; left: 0; right: 0; top: 322px; text-align: center;
    font-size: 14px; letter-spacing: 1px; color: var(--ink-soft);
  }
  /* front side */
  .card--front .brand-row {
    position: absolute; left: 40px; top: 150px; display: flex; align-items: center; gap: 12px;
  }
  .card--front .brand__name { font-size: 22px; letter-spacing: 3px; line-height: 1.2; text-align: left; }
  .card--front .brand__square { width: 14px; height: 14px; }
  .team-photo {
    position: absolute; left: 225px; top: 205px; width: 105px; height: 70px;
    background: linear-gradient(90deg, var(--photo-a) 0%, var(--photo-b) 100%);
  }
  .divider { position: absolute; left: 355px; top: 140px; width: 1px; height: 150px; background: var(--ink-soft); }
  .contact { position: absolute; left: 380px; top: 140px; }
  .contact__name { font-family: "Roboto", sans-serif; font-size: 27px; letter-spacing: 1px; text-transform: uppercase; }
  .contact__license { font-size: 16px; letter-spacing: 1px; margin: 8px 0 14px; }
  .contact__list { list-style: none; }
  .contact__item { display: flex; align-items: center; gap: 10px; font-size: 19px; letter-spacing: .5px; line-height: 1.45; }
  .contact__item svg { width: 13px; height: 13px; flex: none; }
</style>
</head>
<body>
<main class="stage">
  <section class="card card--back" aria-label="Card back">
    <div class="brand">
      <span class="brand__square"></span>
      <p class="brand__name">Tesmaro<br>Realty</p>
    </div>
    <p class="address">57 Oleander Ct. , Wailea HI 96721</p>
  </section>

  <section class="card card--front" aria-label="Card front">
    <div class="brand-row">
      <span class="brand__square"></span>
      <p class="brand__name">Tesmaro<br>Realty</p>
    </div>
    <div class="team-photo" role="img" aria-label="Portrait photo of the two agents"></div>
    <div class="divider"></div>
    <div class="contact">
      <h1 class="contact__name">Lina Tesmaro R(S)</h1>
      <p class="contact__license">LIC.# 41927</p>
      <ul class="contact__list">
        <li class="contact__item">
          <svg viewBox="0 0 16 16" aria-hidden="true"><path fill="#fff" d="M3 1l3 3-1.5 2c1 2 2.5 3.5 4.5 4.5L11 9l3 3-2 2C6 14 2 10 1 3z"/></svg>
          808 555-0163
        </li>
        <li class="contact__item">
          <svg viewBox="0 0 16 16" aria-hidden="true"><rect x="1.5" y="3.5" width="13" height="9" fill="none" stroke="#fff" stroke-width="1.5"/><path d="M1.5 3.5L8 9l6.5-5.5" fill="none" stroke="#fff" stroke-width="1.5"/></svg>
          Lina@Tesmaro.net
        </li>
        <li class="contact__item">
          <svg viewBox="0 0 16 16" aria-hidden="true"><circle cx="8" cy="8" r="6.5" fill="none" stroke="#fff" stroke-width="1.3"/><ellipse cx="8" cy="8" rx="2.8" ry="6.5" fill="none" stroke="#fff" stroke-width="1.1"/><path d="M1.5 8h13" stroke="#fff" stroke-width="1.1"/></svg>
          www.PeakHomeFinds.com
        </li>
      </ul>
    </div>
  </section>
</main>
</body>
</html>
```